Modern & Aesthetic Electrician Sign Design for Work Vehicle

Modern and aesthetic signage design for an electricians work vehicle. Including already designed logo, mobile number, ABN, licensing number and services offered. Preference is black background, symmetric design with logo centred, services offered at bottom of sign in smaller size font. Mobile number readable and big enough to standout without being too large.

Industry/Entity Type

Electrician

Font styles to use
Serif
Sans Serif

Colors
000000
ffffff
ec1f27

Requirements
Must have
• Logo
• Services Offered
• Mobile Number
• ABN
• License Number
• Black background

```html
<!DOCTYPE html>
<html lang="en">
<head>
<meta charset="utf-8">
<title>Kestrel Electrical – Vehicle Sign</title>
<link rel="stylesheet" href="https://fonts.googleapis.com/css2?family=Exo+2:wght@400;700;800&display=swap">
<style>
  :root {
    --page-bg: #e6e6e6;
    --sign-black: #1c1c1c;
    --sign-charcoal: #3a3a3a;
    --brand-red: #ec1f27;
    --red-deep: #a5191b;
    --white: #ffffff;
  }
  * { margin: 0; padding: 0; box-sizing: border-box; }
  html, body { width: 1200px; height: 1106px; overflow: hidden; }
  body {
    background: var(--page-bg);
    font-family: "Exo 2", sans-serif;
    position: relative;
  }
  .vehicle-sign {
    position: absolute;
    left: 30px;
    top: 350px;
    width: 1140px;
    height: 406px;
    overflow: hidden;
    background: radial-gradient(ellipse at 55% 30%, var(--sign-charcoal), var(--sign-black) 75%);
    box-shadow: 0 4px 12px rgba(0,0,0,.35);
  }
  .sign-shapes { position: absolute; inset: 0; }
  .brand-mark {
    position: absolute;
    left: 118px; top: 61px;
    width: 210px; height: 210px;
    border: 9px solid var(--white);
    border-radius: 50%;
  }
  .brand-name {
    position: absolute;
    left: 64px; top: 272px;
    width: 318px;
    color: var(--white);
    font-weight: 700;
    text-align: center;
    line-height: 1;
  }
  .brand-name .word-main { display: block; font-size: 62px; letter-spacing: 1px; }
  .brand-name .word-sub { display: block; font-size: 19px; letter-spacing: 13px; margin-top: 8px; padding-left: 13px; }
  .services {
    position: absolute;
    left: 478px; top: 52px;
    display: flex;
    color: var(--white);
    font-size: 24px;
    list-style: none;
  }
  .services ul { list-style: none; }
  .services ul:nth-child(1) { width: 221px; }
  .services ul:nth-child(2) { width: 200px; }
  .services li { height: 40.5px; padding-left: 19px; position: relative; }
  .services li::before {
    content: ""; position: absolute; left: 0; top: 12px;
    width: 6px; height: 6px; border-radius: 50%; background: var(--brand-red);
  }
  .contact {
    position: absolute;
    right: 34px; top: 272px;
    color: var(--white);
    text-align: right;
  }
  .contact .phone { font-size: 78px; font-weight: 800; line-height: 1; letter-spacing: 1px; }
  .contact .credentials { font-size: 31px; font-weight: 400; margin-top: 6px; }
  .contact .credentials b { font-weight: 800; }
</style>
</head>
<body>
  <section class="vehicle-sign">
    <svg class="sign-shapes" width="1140" height="406" viewBox="0 0 1140 406">
      <defs>
        <linearGradient id="redBand" x1="0" y1="0" x2="1" y2="1">
          <stop offset="0" stop-color="var(--red-deep)"/>
          <stop offset=".5" stop-color="var(--brand-red)"/>
          <stop offset="1" stop-color="var(--red-deep)"/>
        </linearGradient>
      </defs>
      <path d="M0 208 C 260 300, 760 262, 1140 104 L1140 406 L0 406 Z" fill="url(#redBand)"/>
      <path d="M220 268 C 560 282, 900 220, 1140 104 L1140 120 C 900 232, 560 290, 220 268 Z" fill="var(--white)"/>
    </svg>

    <div class="brand-mark"></div>
    <div class="brand-name">
      <span class="word-main">KESTREL</span>
      <span class="word-sub">ELECTRICAL</span>
    </div>

    <div class="services">
      <ul>
        <li>Lorem ipsum</li>
        <li>Dolor sit</li>
        <li>Consectetur</li>
        <li>Consectetur</li>
      </ul>
      <ul>
        <li>Ut enim ad</li>
        <li>Duis aute</li>
        <li>Laborum</li>
      </ul>
      <ul>
        <li>Lorem ipsum</li>
        <li>Dolor sit</li>
      </ul>
    </div>

    <div class="contact">
      <p class="phone">123-456-789</p>
      <p class="credentials"><b>License Number</b> 01234&nbsp; <b>ABN</b> 01234</p>
    </div>
  </section>
</body>
</html>
```